Ward Compass Business Card Design*

We need a business card design for our company Ward Compass. Our company is specialized in providing online consulting services regarding medical institutions, hospitals and doctors. We work with patients worldwide looking to choose between healthcare providers. We have a website you may use as a reference, where we list doctors and clinics worldwide. So we target Medical providers as well as patients worldwide.
Target Market(s)
Medical Providers and patients around the world
Industry/Entity Type
Medical
Contact Information for Business Card
Salma Derkaoui
CEO
+90 612 348 2071
info@wardcompass-example.com
www.wardcompass-example.com
14 Annakhil 3 H.R.B. Rabat, Morocco
Requirements
Must have
- Company logo/name on one full side, personal info and smaller logo and company name on the other side.
Nice to have
- Smart and elegant design

```html
<!DOCTYPE html>
<html lang="en">
<head>
<meta charset="utf-8">
<title>Ward Compass Business Card</title>
<link href="https://fonts.googleapis.com/css2?family=Montserrat:wght@400;600;700&family=Arimo:wght@400;700&display=swap" rel="stylesheet">
<style>
  :root {
    --backdrop: #2a2a2c;
    --card-white: #ffffff;
    --brand-navy: #1d3c6b;
    --panel-blue: #16406b;
    --stripe-grey: #8a8a8c;
    --text-light: #ffffff;
  }
  * { margin: 0; padding: 0; box-sizing: border-box; }
  html, body {
    width: 1200px; height: 880px; overflow: hidden;
    background: var(--backdrop);
  }
  .canvas {
    position: relative; width: 1200px; height: 880px;
  }
  .card {
    position: absolute; left: 250px; width: 700px; height: 400px;
    border-radius: 24px; overflow: hidden; background: var(--card-white);
    box-shadow: 0 14px 30px rgba(0,0,0,0.45);
  }
  .card--front { top: 24px; }
  .card--back { top: 456px; }

  .brand {
    position: absolute; display: flex; align-items: center; gap: 14px;
  }
  .brand__dot {
    width: 44px; height: 44px; border-radius: 50%; background: var(--brand-navy);
    flex: none;
  }
  .brand__name {
    font-family: "Montserrat", sans-serif; font-weight: 600;
    color: var(--brand-navy); text-transform: uppercase;
    letter-spacing: 1px; white-space: nowrap;
  }
  .card--front .brand { left: 190px; top: 176px; }
  .card--front .brand__name { font-size: 34px; }
  .card--back .brand { left: 56px; top: 214px; }
  .card--back .brand .brand__dot { width: 36px; height: 36px; }
  .card--back .brand__name { font-size: 27px; }

  .back-shapes { position: absolute; inset: 0; }
  .back-shapes .stripe { fill: var(--stripe-grey); }
  .back-shapes .gap { fill: var(--card-white); }
  .back-shapes .panel { fill: var(--panel-blue); }

  .contact {
    position: absolute; left: 482px; top: 92px; color: var(--text-light);
    font-family: "Arimo", Arial, sans-serif;
  }
  .contact__name { font-size: 20px; letter-spacing: 0.3px; }
  .contact__name strong { font-weight: 700; }
  .contact__role { font-size: 15px; margin-top: 4px; }
  .contact__list { list-style: none; margin-top: 44px; }
  .contact__item {
    display: flex; align-items: center; gap: 9px;
    font-size: 12.5px; margin-bottom: 11px; white-space: nowrap;
  }
  .contact__icon { width: 18px; height: 18px; flex: none; }
</style>
</head>
<body>
<main class="canvas">
  <section class="card card--front" aria-label="Business card front">
    <div class="brand">
      <span class="brand__dot"></span>
      <span class="brand__name">Ward Compass</span>
    </div>
  </section>

  <section class="card card--back" aria-label="Business card back">
    <svg class="back-shapes" width="700" height="400" viewBox="0 0 700 400">
      <path class="stripe" d="M288 0 C418 70 463 210 446 400 L700 400 L700 0 Z"/>
      <path class="gap" d="M300 0 C428 70 471 210 456 400 L700 400 L700 0 Z"/>
      <path class="panel" d="M305 0 C433 70 476 210 461 400 L700 400 L700 0 Z"/>
    </svg>

    <div class="brand">
      <span class="brand__dot"></span>
      <span class="brand__name">Ward Compass</span>
    </div>

    <div class="contact">
      <p class="contact__name"><strong>SALMA</strong> DERKAOUI</p>
      <p class="contact__role">CEO</p>
      <ul class="contact__list">
        <li class="contact__item">
          <svg class="contact__icon" viewBox="0 0 18 18" aria-hidden="true">
            <circle cx="9" cy="9" r="8" fill="none" stroke="#fff" stroke-width="1.3"/>
            <path d="M6 5.5 L7.6 5.5 L8.2 7.4 L7.3 8.2 Q8.2 10 9.8 10.8 L10.6 9.9 L12.5 10.5 L12.5 12 Q8 12.5 6 5.5 Z" fill="#fff"/>
          </svg>
          <span>+90 612 348 2071</span>
        </li>
        <li class="contact__item">
          <svg class="contact__icon" viewBox="0 0 18 18" aria-hidden="true">
            <circle cx="9" cy="9" r="8" fill="none" stroke="#fff" stroke-width="1.3"/>
            <rect x="5" y="6" width="8" height="6" fill="none" stroke="#fff" stroke-width="1.1"/>
            <path d="M5 6 L9 9.3 L13 6" fill="none" stroke="#fff" stroke-width="1.1"/>
          </svg>
          <span>info@wardcompass-example.com</span>
        </li>
        <li class="contact__item">
          <svg class="contact__icon" viewBox="0 0 18 18" aria-hidden="true">
            <circle cx="9" cy="9" r="8" fill="none" stroke="#fff" stroke-width="1.3"/>
            <circle cx="9" cy="9" r="4.5" fill="none" stroke="#fff" stroke-width="1"/>
            <ellipse cx="9" cy="9" rx="2" ry="4.5" fill="none" stroke="#fff" stroke-width="1"/>
            <path d="M4.5 9 H13.5" stroke="#fff" stroke-width="1"/>
          </svg>
          <span>www.wardcompass-example.com</span>
        </li>
      </ul>
    </div>
  </section>
</main>
</body>
</html>
```